Orthopedic Arm Surgeon Brochure

Bifold modern design. I will supply the text, my photo, and photos of my textbooks. Prefer colors in the greens, blues, greys. For more information visit LimbForwardClinic.com Please feel free to e-mail me with any questions. Current brochure attached; I want to modernize this, get rid of frames, and change the text.

Target Market(s)

High-end market

Colors
3176b5
33a6d7
33b8a4
abd036
876aae
b768aa

Requirements
Must have
• Beautiful finishes
Should not have
• Bright reds, yellows, oranges that emit fear

```html
<!DOCTYPE html>
<html lang="en">
<head>
<meta charset="utf-8">
<title>Orthopedic Arm Surgery Brochure</title>
<link href="https://fonts.googleapis.com/css2?family=Roboto+Condensed:wght@400;700&family=Open+Sans:wght@400;600;700&display=swap" rel="stylesheet">
<style>
  :root{
    --green:#9cc83a;
    --green-deep:#7fae22;
    --charcoal:#48494b;
    --charcoal-dark:#3a3b3d;
    --paper:#f2f2f2;
    --paper-shade:#dedede;
    --ink:#333;
    --backdrop:#d3d3d3;
    --white:#fff;
  }
  *{box-sizing:border-box;margin:0;padding:0}
  html,body{width:1200px;height:792px;overflow:hidden;background:var(--backdrop)}
  body{position:relative;font-family:"Open Sans",Arial,sans-serif}
  .spread{position:absolute;top:206px;width:588px;height:380px;background:var(--paper);box-shadow:0 4px 14px rgba(0,0,0,.25);overflow:hidden}
  .spread--outer{left:8px}
  .spread--inner{left:604px}
  .spread svg{position:absolute;inset:0}
  .fold{position:absolute;top:0;left:293px;width:2px;height:380px;background:linear-gradient(90deg,rgba(0,0,0,.12),rgba(255,255,255,.4))}
  .txt{position:absolute}
  .service-list{font-family:"Roboto Condensed",Arial,sans-serif;font-weight:700;color:var(--white);font-size:11px;line-height:1.25;text-transform:uppercase;letter-spacing:.2px;list-style:none}
  .service-list--bulleted li::before{content:"";display:inline-block;width:5px;height:5px;background:var(--white);margin-right:5px;vertical-align:1px}
  .contact{font-family:"Roboto Condensed",Arial,sans-serif;color:var(--charcoal-dark);line-height:1.2}
  .contact .phone{font-size:11px}
  .contact .web{font-size:12px;font-weight:700}
  .booking{display:flex;align-items:center;gap:4px;font-family:"Roboto Condensed",Arial,sans-serif;font-weight:700;font-size:12px;color:var(--charcoal-dark)}
  .booking .dot{width:14px;height:14px;border-radius:50%;background:var(--charcoal-dark)}
  .brand{font-family:"Roboto Condensed",Arial,sans-serif;font-weight:700;font-size:12px;line-height:1.1;color:var(--charcoal-dark);text-align:center}
  .brand .brand-sub{font-weight:700;font-size:9px}
  .section-tag{position:absolute;font-family:"Roboto Condensed",Arial,sans-serif;font-weight:700;font-size:9px;line-height:1;color:var(--charcoal-dark);background:var(--green);padding:3px 6px;text-transform:uppercase}
  .section-title{position:absolute;font-family:"Roboto Condensed",Arial,sans-serif;font-weight:700;font-size:10px;color:var(--charcoal);text-transform:uppercase;letter-spacing:.3px}
  .body-copy{position:absolute;font-size:5.2px;line-height:1.4}
  .body-copy--light{color:#f0f0f0}
  .body-copy--dark{color:var(--ink)}
  .body-copy .link{font-weight:700;color:var(--green)}
  .body-copy--dark .link{color:var(--green-deep)}
</style>
</head>
<body>

<!-- Outer spread: back cover + front cover -->
<section class="spread spread--outer">
  <svg width="588" height="380" viewBox="0 0 588 380">
    <defs>
      <linearGradient id="paperFade" x1="0" y1="0" x2="0" y2="1">
        <stop offset="0" stop-color="#f7f7f7"/><stop offset="1" stop-color="#dcdcdc"/>
      </linearGradient>
      <linearGradient id="portraitTone" x1="0" y1="0" x2="1" y2="1">
        <stop offset="0" stop-color="#e9e9e9"/><stop offset=".6" stop-color="#6b5a52"/><stop offset="1" stop-color="#2a2a2e"/>
      </linearGradient>
      <linearGradient id="shoulderTone" x1="0" y1="0" x2="0" y2="1">
        <stop offset="0" stop-color="#7a6a62"/><stop offset="1" stop-color="#3c3c40"/>
      </linearGradient>
      <linearGradient id="bookTone" x1="0" y1="0" x2="0" y2="1">
        <stop offset="0" stop-color="#c9b47a"/><stop offset=".35" stop-color="#3b4a8a"/><stop offset=".55" stop-color="#a32a3a"/><stop offset=".8" stop-color="#2f5fa8"/><stop offset="1" stop-color="#3a8fd0"/>
      </linearGradient>
    </defs>

    <!-- back cover -->
    <rect class="page-bg" x="0" y="0" width="294" height="380" fill="url(#paperFade)"/>
    <rect class="book-strip" x="0" y="0" width="40" height="380" fill="var(--green)"/>
    <rect role="img" aria-label="Stack of the surgeon's hand surgery textbook covers" x="5" y="14" width="30" height="352" fill="url(#bookTone)"/>
    <rect role="img" aria-label="Portrait of the surgeon in a dark suit" x="60" y="0" width="234" height="215" fill="url(#portraitTone)"/>
    <path class="back-panel" d="M40 270 Q140 185 294 205 L294 330 L40 330 Z" fill="var(--charcoal)"/>
    <path class="back-swoosh" d="M40 262 Q140 178 294 198" fill="none" stroke="var(--green)" stroke-width="5"/>
    <path class="back-band" d="M40 330 Q170 300 294 318 L294 380 L40 380 Z" fill="var(--green)"/>

    <!-- front cover -->
    <rect class="page-bg" x="294" y="0" width="294" height="380" fill="url(#paperFade)"/>
    <path class="front-top-curve" d="M294 0 L420 0 Q330 40 330 140 L294 150 Z" fill="var(--green)"/>
    <rect role="img" aria-label="Man in a grey jacket holding his painful shoulder" x="360" y="18" width="110" height="200" fill="url(#shoulderTone)"/>
    <path class="front-panel" d="M588 120 Q480 140 470 200 Q455 228 294 230 L294 330 L588 330 Z" fill="var(--charcoal)"/>
    <path class="front-swoosh" d="M588 40 Q500 70 492 150 Q486 205 440 222" fill="none" stroke="var(--charcoal-dark)" stroke-width="10"/>
    <path class="front-swoosh-light" d="M588 112 Q490 130 474 205" fill="none" stroke="var(--white)" stroke-width="4"/>
    <circle class="logo-disc" cx="530" cy="70" r="54" fill="var(--white)" stroke="var(--charcoal)" stroke-width="5"/>
    <path class="front-band" d="M294 322 Q420 300 588 318 L588 380 L294 380 Z" fill="var(--green)"/>
  </svg>
  <div class="fold"></div>

  <ul class="txt service-list" style="left:95px;top:240px;text-align:right;width:180px">
    <li>Carpal Tunnel</li><li>Cubital Tunnel</li><li>Trigger Finger</li><li>DeQuervain's Tendinitis</li><li>Elbow &amp; Shoulder Pain</li>
  </ul>
  <div class="txt contact" style="left:52px;top:344px"><div class="phone">555-014-2270</div><div class="web">www.LimbForwardClinic.com</div></div>
  <div class="txt booking" style="left:205px;top:328px"><span class="dot"></span>CareBook</div>

  <div class="txt brand" style="left:486px;top:54px;width:88px">NORTHGATE<br><span class="brand-sub">Orthopedic Partners</span></div>
  <ul class="txt service-list service-list--bulleted" style="left:312px;top:242px">
    <li>Carpal Tunnel</li><li>Cubital Tunnel</li><li>Trigger Finger</li><li>DeQuervain's Tendinitis</li><li>Elbow &amp; Shoulder Pain</li>
  </ul>
  <div class="txt contact" style="left:310px;top:344px"><div class="phone">555-014-2270</div><div class="web">www.LimbForwardClinic.com</div></div>
  <div class="txt booking" style="left:505px;top:336px"><span class="dot"></span>CareBook</div>
</section>

<!-- Inner spread -->
<section class="spread spread--inner">
  <svg width="588" height="380" viewBox="0 0 588 380">
    <defs>
      <linearGradient id="lightFade" x1="0" y1="0" x2="0" y2="1">
        <stop offset="0" stop-color="#fafafa"/><stop offset="1" stop-color="#d9d9d9"/>
      </linearGradient>
      <linearGradient id="wristTone" x1="0" y1="0" x2="1" y2="1">
        <stop offset="0" stop-color="#eae6e0"/><stop offset=".6" stop-color="#3a6fb0"/><stop offset="1" stop-color="#2b3f66"/>
      </linearGradient>
      <linearGradient id="bandageTone" x1="0" y1="0" x2="1" y2="1">
        <stop offset="0" stop-color="#4aa0d8"/><stop offset=".5" stop-color="#e8e8e8"/><stop offset="1" stop-color="#2f6fae"/>
      </linearGradient>
      <clipPath id="leftCircle"><circle cx="198" cy="112" r="92"/></clipPath>
      <clipPath id="rightCircle"><circle cx="372" cy="86" r="104"/></clipPath>
    </defs>

    <rect x="0" y="0" width="588" height="380" fill="url(#lightFade)"/>

    <!-- left page -->
    <path class="carpal-panel" d="M0 40 Q80 10 150 30 L294 30 L294 220 Q150 240 0 280 Z" fill="var(--charcoal)"/>
    <path class="carpal-swoosh" d="M0 290 Q150 246 294 230" fill="none" stroke="var(--green)" stroke-width="5"/>
    <circle cx="198" cy="112" r="98" fill="var(--charcoal-dark)"/>
    <rect role="img" aria-label="Man in a blue sweater holding his sore wrist" x="104" y="18" width="190" height="190" clip-path="url(#leftCircle)" fill="url(#wristTone)"/>

    <!-- right page -->
    <path class="trigger-panel" d="M294 0 L588 0 L588 230 Q440 232 294 262 Z" fill="var(--charcoal)"/>
    <path class="trigger-swoosh" d="M294 268 Q440 238 588 236" fill="none" stroke="var(--green)" stroke-width="5"/>
    <circle cx="372" cy="86" r="110" fill="var(--white)"/>
    <rect role="img" aria-label="Bandaged hand after surgery held by a gloved clinician" x="268" y="0" width="208" height="190" clip-path="url(#rightCircle)" fill="url(#bandageTone)"/>
    <rect class="wrist-panel" x="294" y="270" width="294" height="110" fill="#ececec" opacity=".6"/>
  </svg>
  <div class="fold"></div>

  <div class="section-tag" style="left:10px;top:44px">Carpal Tunnel<br>Syndrome</div>
  <p class="body-copy body-copy--light" style="left:10px;top:68px;width:80px">Carpal tunnel syndrome happens when the median nerve is squeezed at the wrist. It can bring numbness, tingling and weakness in the thumb and fingers, often at night or while holding a phone, steering wheel or book. Early care with splints and rest can ease symptoms. When they persist, a short outpatient release relieves the pressure and most patients return to daily tasks quickly. To see a video of the procedure please go to: <span class="link">www.LimbForwardClinic.com</span></p>

  <div class="section-title" style="left:130px;top:294px">Cubital Tunnel Syndrome</div>
  <p class="body-copy body-copy--dark" style="left:22px;top:310px;width:256px;text-align:center">Cubital tunnel syndrome occurs when the ulnar nerve is pinched at the elbow, causing numbness in the ring and small fingers. Avoiding long bends of the elbow and padding hard surfaces often helps. If this fails, a minimally invasive release allows an early return to activity with a low rate of complications. To see a video please go to: <span class="link">www.LimbForwardClinic.com</span></p>

  <div class="section-tag" style="left:488px;top:8px">Trigger Finger</div>
  <p class="body-copy body-copy--light" style="left:488px;top:28px;width:90px">Trigger finger occurs when the tendon that bends the finger catches in its sheath, causing clicking, locking and pain. Splinting and an injection often solve the problem. If triggering returns, a minor outpatient release restores smooth motion and is almost always a permanent cure. To see a video please go to: <span class="link">www.LimbForwardClinic.com</span></p>

  <div class="section-title" style="left:410px;top:272px">Wrist Pain</div>
  <p class="body-copy body-copy--dark" style="left:310px;top:288px;width:264px;text-align:center">Wrist pain has many causes and the diagnosis is best made by a fellowship-trained hand surgeon. A common cause is De Quervain's tendinitis, which brings pain on the thumb side of the wrist when lifting, gripping or carrying a child. Rest, a brace and one injection usually help. If pain persists, a small outpatient release is very effective and patients return to activity soon after. To see a video please go to: <span class="link">www.LimbForwardClinic.com</span></p>
</section>

</body>
</html>
```